Book cover for book about Climate Change

Looking for a clean, bold, and attractive cover for a mass-market paperback (5.5"x 8.5") about solving the climate change problem. Title is either "When Rivers Learn to Sing” or A Lantern Over Quiet Fields” (your choice), subtitle is "A five-step plan to reverse climate change — to ensure that your grandchildren will live on a clean and comfortable planet," author is Dale Pruitt. Thinking that it *might* feature an image of Earth (or a portion thereof) and its very thin layer of atmosphere -- but STRONGLY encourage other ideas too!

Requirements
Nice to have
• Keep it positive — NOT scary doom-and-gloom

```html
<!DOCTYPE html>
<html lang="en">
<head>
<meta charset="utf-8">
<title>A Lantern Over Quiet Fields — Dale Pruitt</title>
<link rel="stylesheet" href="https://fonts.googleapis.com/css2?family=Bebas+Neue&family=Montserrat:wght@400;800&family=Oswald:wght@700&display=swap">
<style>
  :root {
    --leaf-light: #1f9a1f;
    --leaf-mid: #0f6e12;
    --leaf-dark: #063a08;
    --night: #020502;
    --title-white: #ffffff;
    --title-shade: #b9bcb9;
    --author-green: #12921a;
    --earth-blue: #2f5fa8;
    --earth-deep: #0d2350;
    --hand-skin: #d9b48f;
  }
  * { margin: 0; padding: 0; box-sizing: border-box; }
  html, body { width: 800px; height: 1200px; overflow: hidden; background: var(--night); }
  .cover {
    position: relative;
    width: 800px;
    height: 1200px;
    overflow: hidden;
    background:
      repeating-linear-gradient(-32deg, rgba(255,255,255,0.035) 0 2px, transparent 2px 46px),
      linear-gradient(180deg, var(--leaf-light) 0%, var(--leaf-mid) 45%, var(--leaf-dark) 72%, var(--night) 90%);
  }
  .title {
    position: absolute;
    top: 100px;
    left: 0;
    width: 800px;
    text-align: center;
    font-family: "Bebas Neue", "Oswald", sans-serif;
    font-weight: 400;
    line-height: 0.9;
    color: var(--title-white);
    white-space: nowrap;
  }
  .title-line { display: block; }
  .title-line--top {
    font-size: 150px;
    letter-spacing: 1px;
    background: linear-gradient(180deg, var(--title-white) 55%, var(--title-shade) 100%);
    -webkit-background-clip: text;
    background-clip: text;
    color: transparent;
  }
  .title-line--bottom { font-size: 142px; letter-spacing: 2px; margin-top: 4px; }
  .subtitle {
    position: absolute;
    top: 470px;
    left: 0;
    width: 800px;
    text-align: center;
    font-family: "Montserrat", sans-serif;
    color: var(--title-white);
    text-transform: uppercase;
  }
  .subtitle-lead {
    font-weight: 800;
    font-size: 17px;
    letter-spacing: 4.6px;
    margin-bottom: 16px;
  }
  .subtitle-body {
    font-weight: 400;
    font-size: 16px;
    letter-spacing: 3.2px;
    line-height: 1.6;
  }
  .earth-in-hands {
    position: absolute;
    left: 0;
    top: 620px;
    width: 800px;
    height: 400px;
  }
  .author {
    position: absolute;
    top: 1058px;
    left: 0;
    width: 800px;
    text-align: center;
    font-family: "Oswald", sans-serif;
    font-weight: 700;
    font-size: 88px;
    letter-spacing: 22px;
    padding-left: 22px;
    color: var(--author-green);
    white-space: nowrap;
  }
</style>
</head>
<body>
  <main class="cover">
    <h1 class="title">
      <span class="title-line title-line--top">A LANTERN OVER</span>
      <span class="title-line title-line--bottom">QUIET FIELDS</span>
    </h1>

    <div class="subtitle">
      <p class="subtitle-lead">A 5-step plan to reverse climate change</p>
      <p class="subtitle-body">To ensure that your grandchildren will live<br>on a clean and comfortable planet</p>
    </div>

    <svg class="earth-in-hands" viewBox="0 0 800 400" role="img" aria-label="Photograph of an adult hand holding a small globe of the Earth while a child's hand reaches out to touch it">
      <defs>
        <radialGradient id="globe-tone" cx="0.45" cy="0.4" r="0.65">
          <stop offset="0" stop-color="var(--earth-blue)"/>
          <stop offset="1" stop-color="var(--earth-deep)"/>
        </radialGradient>
        <linearGradient id="skin-tone" x1="0" y1="0" x2="1" y2="0">
          <stop offset="0" stop-color="var(--hand-skin)" stop-opacity="0"/>
          <stop offset="1" stop-color="var(--hand-skin)" stop-opacity="0.55"/>
        </linearGradient>
      </defs>
      <rect x="420" y="20" width="380" height="380" fill="url(#skin-tone)"/>
      <circle cx="400" cy="210" r="160" fill="url(#globe-tone)"/>
    </svg>

    <p class="author">DALE PRUITT</p>
  </main>
</body>
</html>
```